New Flyer Design Project

Needing brochure explaining the benefits of a home sleep study compared to a clinical hospital sleep study. We had our company logo designed by Lumen Forge, we love it. We would like for it to be a bi-fold. See attachments for examples of information we would like to include.

```html
<!DOCTYPE html>
<html lang="en">
<head>
<meta charset="utf-8">
<title>Home Sleep Study Bi-fold Brochure</title>
<link rel="stylesheet" href="https://fonts.googleapis.com/css2?family=Antonio:wght@500;600&family=Fira+Sans+Extra+Condensed:ital,wght@0,400;0,600;0,700;1,400;1,600&display=swap">
<style>
:root{
  --green:#6aa83a;
  --green-dark:#5b9a2f;
  --lime:#c9dd16;
  --navy:#012b5c;
  --blue:#0a9ad8;
  --ink:#0d2f5e;
  --backdrop:#d9dbda;
  --white:#ffffff;
}
*{box-sizing:border-box;margin:0;padding:0}
html,body{width:1200px;height:1200px;overflow:hidden;background:var(--backdrop)}
.stage{position:absolute;left:0;top:0;width:1932px;height:1932px;transform:scale(0.62112);transform-origin:0 0;font-family:"Fira Sans Extra Condensed",sans-serif;color:var(--ink)}
.spread{position:absolute;left:426px;width:1080px;overflow:hidden;background:var(--white)}
.spread--outside{top:112px;height:834px}
.spread--inside{top:986px;height:832px}
.abs{position:absolute}
.head{font-family:"Antonio",sans-serif;font-weight:600;letter-spacing:0;white-space:nowrap}

/* outside – left panel */
.steps-panel{left:0;top:0;width:540px;height:834px;background:var(--green)}
.steps-title{left:0;top:60px;width:540px;text-align:center;color:var(--white);font-size:31px;line-height:34px}
.steps-intro{left:0;top:146px;width:540px;height:57px;background:var(--lime);text-align:center;font-weight:600;font-size:15.5px;line-height:22px;padding:6px 70px 0;color:var(--navy)}
.step{left:126px;width:40px;height:40px}
.step-text{left:215px;width:212px;color:var(--white);font-size:15.5px;line-height:21.6px}
.step-text b{font-weight:700}
.tagline{left:0;top:580px;width:540px;text-align:center;color:var(--white);font-size:28px}
.tagline-sub{left:0;top:625px;width:540px;text-align:center;color:var(--white);font-size:19px;line-height:25px}
.contact-lead{left:0;top:728px;width:540px;text-align:center;color:var(--white);font-size:18px}
.contact-item{color:var(--white);font-size:15px;line-height:16px}
.contact-icon{width:12px;height:12px}

/* outside – cover */
.cover-fade{left:540px;top:0;width:540px;height:834px;background:linear-gradient(180deg,#fff 0%,#fff 22%,#e6e7e8 60%,#d5d6d8 100%)}
.brand{left:560px;top:30px;display:flex;align-items:center;gap:10px}
.brand-dot{width:22px;height:22px;border-radius:50%;background:var(--green)}
.brand-name{font-size:30px;font-weight:600;color:var(--navy)}
.cover-photo{left:724px;top:270px;width:356px;height:500px;background:radial-gradient(ellipse at 55% 30%,#c9a38a 0%,#7f8fb0 30%,#f0f0f2 62%,#dcd8d2 100%)}
.cover-title{left:540px;top:108px;width:540px;text-align:center;font-size:68px;line-height:74px}
.cover-title .l1{color:var(--navy)}
.cover-title .l2{color:var(--green)}
.cover-sub{left:572px;top:288px;width:230px;font-size:23px;line-height:32px;color:var(--navy)}
.cover-sub b{font-weight:600}
.cover-foot{left:540px;top:758px;width:540px;text-align:center;color:var(--white)}
.cover-foot .name{font-size:19px;font-weight:600}
.cover-foot .line{font-size:18px;font-style:italic;margin-top:4px}

/* inside – left */
.topic-icon{left:76px;width:70px;height:70px}
.topic{left:178px;width:300px}
.topic h3{color:var(--green);font-size:21px;line-height:26px;margin-bottom:2px}
.topic p{font-size:15.5px;line-height:21.6px;color:var(--navy)}
.rule{left:64px;width:412px;height:1px;background:var(--green)}
.sensor{width:84px;height:84px;border-radius:50%;border:3px solid var(--green);background:var(--white);padding:6px}
.sensor-img{width:100%;height:100%;border-radius:50%}
.sensor-cap{width:140px;text-align:center;color:var(--green-dark);font-size:12.5px;line-height:18px;font-style:italic;font-weight:600}

/* inside – right */
.compare-title{left:540px;top:56px;width:540px;text-align:center;color:var(--green);font-size:29px}
.compare-intro{left:579px;top:116px;width:460px;font-size:15.5px;line-height:21.6px;color:var(--navy)}
.compare{left:579px;top:196px;width:457px;border-collapse:separate;border-spacing:0;border:1px solid var(--navy);border-radius:8px;overflow:hidden;font-size:15px;line-height:21.6px;text-align:center;color:var(--navy);background:var(--white);table-layout:fixed}
.compare th{height:48px;color:var(--white);font-weight:600;font-size:13.5px;line-height:15px;text-transform:uppercase;background:var(--navy);padding:0 8px}
.compare th.col-home{background:var(--green)}
.compare td{border-top:1px solid var(--navy);border-left:1px solid var(--navy);vertical-align:top;padding:12px 4px 0}
.compare td:first-child{border-left:none;font-weight:600}
.compare tr.r-std td{height:65px}
.compare tr.r-tall td{height:88px}
.compare tr.r-last td{height:71px}
.advantage{left:579px;top:627px;width:457px;height:164px;background:var(--green);border-radius:4px;padding:16px 20px;color:var(--white)}
.advantage h4{font-weight:400;font-size:23px;margin-bottom:6px}
.advantage p{font-size:15px;line-height:21.6px}
</style>
</head>
<body>
<div class="stage">

  <!-- OUTSIDE SPREAD -->
  <section class="spread spread--outside">
    <div class="abs steps-panel"></div>
    <div class="abs cover-fade"></div>
    <div class="abs cover-photo" role="img" aria-label="Photo of a woman sleeping peacefully in her own bed wearing a home sleep test device, with a bedside clock"></div>

    <svg class="abs" style="left:0;top:0" width="1080" height="834" viewBox="0 0 1080 834" aria-hidden="true">
      <path d="M0 622 C90 690 200 720 320 700 C420 684 470 650 540 660 L540 834 L0 834 Z" fill="#0a9ad8"/>
      <path d="M0 650 C110 720 240 730 360 690 C440 664 500 650 540 660 L540 834 L0 834 Z" fill="#0d8fcf" opacity=".6"/>
      <path d="M0 680 C120 720 250 720 380 690 C450 674 500 656 540 660 L540 834 L0 834 Z" fill="#012b5c"/>
      <path d="M540 660 C620 650 700 670 780 700 C880 740 980 720 1080 652 L1080 834 L540 834 Z" fill="#6aa83a"/>
      <path d="M540 690 C640 690 720 720 800 740 C900 760 990 720 1080 670 L1080 834 L540 834 Z" fill="#0a9ad8"/>
      <path d="M540 700 C640 700 720 730 800 748 C900 770 990 735 1080 686 L1080 834 L540 834 Z" fill="#012b5c"/>
    </svg>

    <h2 class="abs head steps-title">3 SIMPLE STEPS<br>TO RECLAIM YOUR ENERGY</h2>
    <p class="abs steps-intro">Improving your sleep shouldn't be stressful. At Prairie Rest Sleep Care, we make the process completely seamless:</p>

    <svg class="abs step" style="top:238px" viewBox="0 0 40 40" aria-hidden="true" fill="#fff">
      <rect x="12" y="2" width="24" height="13" rx="4"/><circle cx="10" cy="24" r="5"/><circle cx="30" cy="24" r="5"/>
      <path d="M2 40 a8 8 0 0 1 16 0Z M22 40 a8 8 0 0 1 16 0Z"/>
    </svg>
    <p class="abs step-text" style="top:230px"><b>Consultation:</b> Speak with our dedicated team about your sleep symptoms.</p>

    <svg class="abs step" style="top:326px" viewBox="0 0 40 40" aria-hidden="true" fill="none" stroke="#fff" stroke-width="3">
      <path d="M20 4 L36 12 L20 20 L4 12 Z"/><path d="M4 16 V28 L20 36 L36 28 V16"/><path d="M20 22 V36"/>
    </svg>
    <p class="abs step-text" style="top:316px"><b>Pick Up Your Device:</b> Receive a quick, easy demonstration on how to wear the lightweight device.</p>

    <svg class="abs step" style="top:440px" viewBox="0 0 40 40" aria-hidden="true" fill="#fff">
      <rect x="6" y="8" width="28" height="22" rx="3" fill="none" stroke="#fff" stroke-width="3"/><circle cx="20" cy="18" r="5"/>
      <rect x="2" y="32" width="36" height="4"/><text x="30" y="8" font-size="9" fill="#fff">z</text>
    </svg>
    <p class="abs step-text" style="top:402px"><b>Sleep &amp; Return:</b> Sleep comfortably at home for one night, return the device the next day, and let our sleep specialists analyze your results to build a customized therapy plan.</p>

    <h3 class="abs head tagline">Sleep Restfully. Live Fully.</h3>
    <p class="abs tagline-sub">Don't let poor sleep affect your heart health,<br>productivity, and long-term well-being.</p>

    <p class="abs contact-lead">Contact us today to schedule your Home Sleep Test!</p>
    <svg class="abs contact-icon" style="left:104px;top:762px" viewBox="0 0 12 12" aria-hidden="true"><path d="M6 0 a4 4 0 0 1 4 4 C10 7 6 12 6 12 S2 7 2 4 a4 4 0 0 1 4-4Z" fill="#0a9ad8"/><circle cx="6" cy="4" r="1.5" fill="#012b5c"/></svg>
    <p class="abs contact-item" style="left:130px;top:762px">1420 W Cedar Ln,<br>Maple Grove, KS 66001</p>
    <svg class="abs contact-icon" style="left:304px;top:764px" viewBox="0 0 12 12" aria-hidden="true"><circle cx="6" cy="6" r="6" fill="#0a9ad8"/><path d="M4 3 L5 5 L4.5 6 Q5.5 7.5 6.5 8 L7 7 L9 8 L8.5 9.5 Q4 9 3 4Z" fill="#fff"/></svg>
    <p class="abs contact-item" style="left:330px;top:763px">+1 555-014-7373</p>
    <svg class="abs contact-icon" style="left:304px;top:790px" viewBox="0 0 12 12" aria-hidden="true"><circle cx="6" cy="6" r="6" fill="#0a9ad8"/><circle cx="6" cy="6" r="2.5" fill="#fff"/></svg>
    <p class="abs contact-item" style="left:330px;top:789px">+1 555-019-5131</p>

    <div class="abs brand"><span class="brand-dot"></span><span class="brand-name">Prairie Rest Sleep Care</span></div>
    <h1 class="abs head cover-title"><span class="l1">Your Guide to a</span><br><span class="l2">Better Night’s Sleep</span></h1>
    <p class="abs cover-sub"><b>Home Sleep Study vs. In-Lab Hospital Study:</b> Why Testing at Home is the Most Comfortable Choice for You.</p>
    <div class="abs cover-foot"><p class="name">Prairie Rest Sleep Care</p><p class="line">Quality Care from the Comfort of Your Home</p></div>
  </section>

  <!-- INSIDE SPREAD -->
  <section class="spread spread--inside">
    <svg class="abs" style="left:0;top:0" width="1080" height="832" viewBox="0 0 1080 832" aria-hidden="true">
      <path d="M0 720 C120 710 250 760 380 775 C460 784 520 760 560 720 L560 832 L0 832 Z" fill="#6aa83a"/>
      <path d="M0 745 C130 740 260 780 390 790 C470 796 530 770 570 730 C650 640 760 610 860 612 C960 614 1030 640 1080 660 L1080 832 L0 832 Z" fill="#012b5c"/>
    </svg>

    <svg class="abs topic-icon" style="top:106px" viewBox="0 0 70 70" aria-hidden="true">
      <path d="M44 10 a16 16 0 1 0 20 20 a18 18 0 0 1-20-20Z" fill="#6aa83a"/>
      <circle cx="26" cy="44" r="17" fill="#6aa83a"/><path d="M26 34 V45 H34" stroke="#fff" stroke-width="3" fill="none"/>
    </svg>
    <div class="abs topic" style="top:66px">
      <h3 class="head">Understanding Sleep Apnea &amp; Your Health</h3>
      <p>Do you often wake up choking, snore loudly, or feel exhausted during the day despite spending hours in bed? These are common warning signs of Obstructive Sleep Apnea (OSA)—a serious medical condition where your breathing repeatedly stops and starts while you sleep.</p>
    </div>
    <div class="abs rule" style="top:236px"></div>

    <svg class="abs topic-icon" style="top:298px" viewBox="0 0 70 70" aria-hidden="true">
      <path d="M6 34 L35 8 L64 34" stroke="#6aa83a" stroke-width="6" fill="none"/>
      <rect x="14" y="30" width="42" height="30" fill="#6aa83a"/><rect x="22" y="36" width="26" height="18" fill="#fff"/>
      <circle cx="35" cy="42" r="4" fill="#6aa83a"/><circle cx="56" cy="20" r="9" fill="#6aa83a" stroke="#fff" stroke-width="2"/>
    </svg>
    <div class="abs topic" style="top:252px">
      <h3 class="head">What Is A Home Sleep Test (HST)?</h3>
      <p>A Home Sleep Test is a modern, diagnostic procedure that monitors your breathing, heart rate, and oxygen levels. Instead of spending the night in a clinical hospital room, this test allows you to gather accurate sleep data right from the comfort of your own bed.</p>
    </div>
    <div class="abs rule" style="top:422px"></div>

    <svg class="abs topic-icon" style="top:450px" viewBox="0 0 70 70" aria-hidden="true">
      <circle cx="35" cy="35" r="28" fill="none" stroke="#6aa83a" stroke-width="4"/>
      <path d="M22 36 L31 45 L49 27" fill="none" stroke="#6aa83a" stroke-width="5" stroke-linecap="round" stroke-linejoin="round"/>
    </svg>
    <div class="abs topic" style="top:438px">
      <h3 class="head">How Simple Is It?</h3>
      <p>You will receive a small, lightweight, and easy-to-use portable device from our clinic. Before going to bed, you simply apply a few minimal sensors:</p>
    </div>

    <div class="abs sensor" style="left:58px;top:561px"><div class="sensor-img" style="background:#1c3f8a" role="img" aria-label="Photo of a chest belt sensor"></div></div>
    <p class="abs sensor-cap" style="left:30px;top:666px">A comfortable belt around your chest to measure breathing effort.</p>
    <div class="abs sensor" style="left:227px;top:561px"><div class="sensor-img" style="background:radial-gradient(circle,#5c7fa8,#d7dde4)" role="img" aria-label="Photo of a finger pulse oximeter clip"></div></div>
    <p class="abs sensor-cap" style="left:199px;top:666px">A small, non-invasive clip on your finger to monitor oxygen levels.</p>
    <div class="abs sensor" style="left:397px;top:561px"><div class="sensor-img" style="background:radial-gradient(circle,#f4f4f4,#dcdcdc)" role="img" aria-label="Photo of a lightweight nasal cannula"></div></div>
    <p class="abs sensor-cap" style="left:369px;top:666px">A lightweight nasal cannula to track your airflow.</p>

    <h2 class="abs head compare-title">Home Sleep Test vs. Hospital In-Lab Study</h2>
    <p class="abs compare-intro">Many patients delay getting tested because they dread the idea of sleeping in an unfamiliar hospital room surrounded by heavy equipment. Here is an honest, clinical comparison:</p>

    <table class="abs compare">
      <thead><tr><th>Valuation Feature Test (HST)</th><th class="col-home">Home Sleep</th><th>In-Lab Hospital Study</th></tr></thead>
      <tbody>
        <tr class="r-std"><td>Location</td><td>Your own<br>familiar bed</td><td>A sterile hospital<br>or lab room</td></tr>
        <tr class="r-std"><td>Comfort Level</td><td>Very High<br>(Move freely)</td><td>Moderate<br>(Dozens of wires/leads)</td></tr>
        <tr class="r-std"><td>Schedule</td><td>Fits your<br>normal routine</td><td>Subject to hospital<br>lab availability</td></tr>
        <tr class="r-tall"><td>Cost Efficiency</td><td>Highly<br>Budget-Friendly</td><td>High cost due to<br>overnight facility<br>fees</td></tr>
        <tr class="r-last"><td>Insurance Approval</td><td>Highly preferred<br>by insurance</td><td>Often requires strict<br>pre- ualifications</td></tr>
      </tbody>
    </table>

    <div class="abs advantage">
      <h4>The Hidden Clinical Advantage: Natural Data</h4>
      <p>Sleeping in a hospital setting often triggers the "First-Night Effect"—a phenomenon where anxiety alters your typical sleep patterns. Testing at home ensures the data collected accurately reflects your real, everyday sleep behavior.</p>
    </div>
  </section>

</div>
</body>
</html>
```